Menu Design

We want to refresh the feel and look of the menu
but we need to keep the same size and contents. The new design should be modern

Target Market(s)

Onboard Passengers

Industry/Entity Type

Airline

Font styles to use
Sans Serif

Colors

Designer to choose colors to be used in the design.

Requirements
Must have
• Same document size and folding and same contents in PDF

```html
<!DOCTYPE html>
<html lang="en">
<head>
<meta charset="utf-8">
<title>Sandwiches Menu</title>
<link rel="stylesheet" href="https://fonts.googleapis.com/css2?family=Marcellus&family=Tajawal:wght@700;800&family=Montserrat:wght@600;700&display=swap">
<style>
  :root {
    --cream: #fbfbf2;
    --teal: #05a7c6;
    --white: #ffffff;
    --bread-light: #e9c9a0;
    --bread-dark: #c0803f;
  }
  * { margin: 0; padding: 0; box-sizing: border-box; }
  html, body { width: 772px; height: 1200px; overflow: hidden; }
  body { background: var(--cream); position: relative; font-family: "Marcellus", serif; }
  .band { position: absolute; left: 0; top: 674px; width: 772px; height: 526px; background: var(--teal); }
  .title-ar {
    position: absolute; top: 52px; left: 0; width: 772px; text-align: center;
    font-family: "Tajawal", sans-serif; font-weight: 800; font-size: 50px; color: var(--teal);
    direction: rtl; line-height: 1;
  }
  .title-en {
    position: absolute; top: 112px; left: 0; width: 772px; text-align: center;
    font-family: "Marcellus", serif; font-size: 94px; color: var(--teal); letter-spacing: 1px; line-height: 1;
  }
  .photo { position: absolute; }
  .price {
    position: absolute; width: 66px; height: 66px; border-radius: 50%;
    display: flex; flex-direction: column; align-items: center; justify-content: center;
    font-family: "Montserrat", sans-serif; line-height: 1; z-index: 2;
  }
  .price::after {
    content: ""; position: absolute; right: 4px; bottom: -5px; width: 14px; height: 14px;
    background: inherit; transform: skewX(-30deg); z-index: -1;
  }
  .price .cur, .price .each { font-size: 6.5px; font-weight: 700; }
  .price .amt { font-size: 14px; font-weight: 700; margin: 1px 0; }
  .price--teal { background: var(--teal); color: var(--white); }
  .price--white { background: var(--white); color: var(--teal); }
  .caption { position: absolute; width: 330px; text-align: center; }
  .caption .ar {
    font-family: "Tajawal", sans-serif; font-weight: 800; font-size: 19px; line-height: 23px; direction: rtl;
  }
  .caption .rule { width: 8px; height: 1px; margin: 4px auto 5px; }
  .caption .en { font-size: 12.5px; line-height: 15.5px; }
  .on-cream .ar, .on-cream .en { color: var(--teal); }
  .on-cream .rule { background: var(--teal); }
  .on-teal .ar, .on-teal .en { color: var(--white); }
  .on-teal .rule { background: var(--white); }
</style>
</head>
<body>
  <div class="band"></div>

  <h1 class="title-ar">الســـندويتشات</h1>
  <h2 class="title-en">SANDWICHES</h2>

  <svg width="0" height="0" style="position:absolute">
    <defs>
      <linearGradient id="bread" x1="0" y1="0" x2="0" y2="1">
        <stop offset="0" stop-color="#c98a4b"/>
        <stop offset="0.55" stop-color="#e3c39a"/>
        <stop offset="1" stop-color="#d9b286"/>
      </linearGradient>
    </defs>
  </svg>

  <!-- Row 1 -->
  <svg class="photo" style="left:71px;top:275px" width="314" height="145" role="img" aria-label="Chicken tikka mayonnaise sandwich in plain focaccia bread">
    <rect x="0" y="20" width="314" height="110" rx="50" fill="url(#bread)"/>
  </svg>
  <div class="price price--teal" style="left:54px;top:241px"><span class="cur">OMR</span><span class="amt">1.300</span><span class="each">EACH</span></div>
  <div class="caption on-cream" style="left:63px;top:426px">
    <p class="ar">ساندوتش دجاج تكا بالمايونيز يقدم<br>في خبز فوكاتشيا سادة</p>
    <div class="rule"></div>
    <p class="en">Chicken Tikka Mayonnaise Sandwich<br>“Served in plain Focaccia Bread”</p>
  </div>

  <svg class="photo" style="left:413px;top:270px" width="273" height="150" role="img" aria-label="Grilled vegetables with cream cheese sandwich in sumac ciabatta bread">
    <rect x="0" y="15" width="273" height="115" rx="50" fill="url(#bread)"/>
  </svg>
  <div class="price price--teal" style="left:400px;top:241px"><span class="cur">OMR</span><span class="amt">1.100</span><span class="each">EACH</span></div>
  <div class="caption on-cream" style="left:402px;top:426px">
    <p class="ar">ساندويتش خضروات مشوية مع جبنة<br>الكريمة تقدم في خبز سياباتا بالسوماك</p>
    <div class="rule"></div>
    <p class="en">Grilled Vegetables with Cream Cheese Sandwich<br>“Served in sumac Ciabatta bread”</p>
  </div>

  <!-- Row 2 -->
  <svg class="photo" style="left:84px;top:565px" width="302" height="134" role="img" aria-label="Grilled vegetables with sundried tomato sandwich in black sesame focaccia">
    <rect x="0" y="8" width="302" height="118" rx="45" fill="url(#bread)"/>
  </svg>
  <div class="price price--teal" style="left:54px;top:527px"><span class="cur">OMR</span><span class="amt">1.100</span><span class="each">EACH</span></div>
  <div class="caption on-teal" style="left:63px;top:713px">
    <p class="ar">ساندويتش خضروات مشوية مع شرائح<br>طماطم مشوية تقدم في خبز الفوكاكو<br>بالسمسم الأسود</p>
    <div class="rule"></div>
    <p class="en">Grilled Vegetables with<br>Sundried Tomato Slices Sandwich<br>“Served in black sesame Focaccia bread”</p>
  </div>

  <svg class="photo" style="left:402px;top:565px" width="302" height="137" role="img" aria-label="Minted lamb kofta mayonnaise sandwich in plain focaccia bread">
    <rect x="0" y="8" width="302" height="120" rx="45" fill="url(#bread)"/>
  </svg>
  <div class="price price--teal" style="left:400px;top:527px"><span class="cur">OMR</span><span class="amt">1.100</span><span class="each">EACH</span></div>
  <div class="caption on-teal" style="left:402px;top:713px">
    <p class="ar">شطيرة كفتة لحم الخروف المفرومة<br>بالمايونيز تقدم في خبز الفوكاكيا<br>السادة</p>
    <div class="rule"></div>
    <p class="en">Minted Lamb Kofta Mayonnaise Sandwich<br>“Served in plain Focaccia bread”</p>
  </div>

  <!-- Row 3 -->
  <svg class="photo" style="left:84px;top:879px" width="288" height="148" role="img" aria-label="Chicken tikka mayonnaise sandwich in sumac ciabatta bread">
    <rect x="0" y="10" width="288" height="128" rx="48" fill="url(#bread)"/>
  </svg>
  <div class="price price--white" style="left:54px;top:841px"><span class="cur">OMR</span><span class="amt">1.100</span><span class="each">EACH</span></div>
  <div class="caption on-teal" style="left:63px;top:1029px">
    <p class="ar">ساندوتش دجاج تكا بالمايونيز يقدم في<br>خبز سياباتا بالسوماك</p>
    <div class="rule"></div>
    <p class="en">Chicken Tikka Mayonnaise Sandwich<br>“Served in sumac Ciabatta bread”</p>
  </div>

  <svg class="photo" style="left:402px;top:874px" width="300" height="155" role="img" aria-label="Paneer masala sandwich in black sesame focaccia bread">
    <rect x="0" y="12" width="300" height="130" rx="50" fill="url(#bread)"/>
  </svg>
  <div class="price price--white" style="left:400px;top:841px"><span class="cur">OMR</span><span class="amt">1.100</span><span class="each">EACH</span></div>
  <div class="caption on-teal" style="left:402px;top:1029px">
    <p class="ar">ساندوتش بانير ماسالا يقدم في<br>خبز فوكاتشيا بالسمسم الأسود</p>
    <div class="rule"></div>
    <p class="en">Paneer Masala Sandwich<br>“Served in black sesame Focaccia bread”</p>
  </div>
</body>
</html>
```